Family Nature Adventure Stay - Thistlebrook Hollow

Thistlebrook Hollow is a low environmental impact children’s farm stay and nature education experience in Devon England which presents families with the opportunity to get closer to nature.

While staying at Thistlebrook Hollow, guests will be encouraged to take part in organised nature and adventure based activities such as bird and butterfly spotting, making camps, mini beast hunts, egg collecting, star gazing, pond dipping and moth nights.

Think of the stuff you wanted to do with your parents when you were nine – fishing with Dad? Making a camp with your new friends? Clay face modelling with Mum? Convey this in your site design.

We need six pages designing:

1. Home Page
2. Accommodation & Booking
3. Events & Activities
4. Location & Interactive Map
5. Meet the Residents
6. Green Credentials

Sites we like:
http://www.fernloftstudio.example/
I love this site
Full screen image slider
Stylish navigation
Very simple

www.corvettawheels.example
Simple design
Full screen slider
Lots of graphics
The feelof summer in the image
Moving navigation bar

http://www.brindlepixel.example/
A really cool front page
If the images shown was a slider even better.
(I'm not hot on the length of the page)

http://platterwick.example/
Really simple design
Very stylish
Slider half page
Great Nav icons
font for contact us

www.9marrowworks.example
very stylish
images
the idea of the photo book
Beautiful fonts

Target Market(s)

Our target market is young families with one or more children between 6 and 14 who love the great outddors

Industry/Entity Type

Education

Requirements
Must have
• General Design
The site in general should be very nature, holiday and children based. The natural environment, quality, adventure and comfort should be at the heart of the site.
A common styling should be used for all pages.
All pages should feature our telephone number.

The styling does not have to use elements from our logo.
Each page should have a common site navigation bar.

1. Home Page
The home page should include a brief description of what we are and what we offer. A simple page is required with a large image slider and may be a couple of other images.

The home page should feature links to our social media sites (Friendbook & Chirper) and the following: Heritage Keepers, Woodland Stewardship Board, Amberhill Lands, Nearby Beaches, Eco Enterprise Honours.

Annexe sleeps 2+2 bed
Stables sleeps 4
Cosyhollow (Yurt) sleeps 4
Pinecushion (Yurt) sleeps 4

Section should include a section for each accommodation include 360° view image, images, descriptions and embedded booking calendar from (slotkeeper.example) that will feature rates and availability.
The section should note that the yurts have private bathrooms with hot showers and flushing toilets.
This section should link to the correct flyout in the interactive map to show the accommodation location.

3. Location & Interactive Map
The location map should show be a zoomable map showing our location in Devon (perhaps an embedded Google map).

The map should show the layout of Thistlebrook hollow and the surrounding area with flyout images on mouse-over of certain areas with textbox descriptions. This includes the location of the accommodation, amenities, animal fields, and special sites of interest. (see SitePlan.gif for our basic map).

4. Activities & Events
This page details what we are about and what is available to see and do on site, next door at the Woodland Stewardship Board and Heritage Keepers sites and nearby in Devon & Cornwall.

Activities include:
Bird and butterfly spotting, making camps, mini beast hunts, hen’s egg collecting, star gazing, pond dipping, moth nights, clay modelling, slingshot range, tree climbing, candle dipping, animal husbandry, dressing up box, story-telling, cycling, trekking, make a bird-box etc.

We intend to have competitions where children can win prizes (Thistlebrook Club)
Calendar of upcoming events
Thistlebrook club and free giveaway bath duck.
Sponsor the animals.

5. Meet the residents
This page should have a cool design like a top trumps page that lists the residents and their main skills and abilities. This could be a slider, gallery based or other cool interactive feature.

The family: Gareth, Rosalind and our daughters Lottie & Imogen

The animals:
Cats – Pebble & Tansy the farm cats
Dogs – Bram & Toffee
Goats – Bella, Bonnie, Bernadette & Beatrix
Sheep – Gus, Wispy & Clodhopper
Chickens – Including Barney, Dusty, Glorious Plumage, Coopsy & Marge
Rabbit & Guinea Pig – Horace and Zippy

The wildlife:
Foxes
Badgers
Deer
Jays
Jackdaws
Sparrows
Frogs
Newts
Water boatmen
The trout
Dippers
Nuthatch
Thrush
Blackbird
Moths & Butterflies

6. Green Credentials
We have tried hard to incorporate green technologies and practices into our site. This page should showcase some of the features we have used.
Central log biomass hot water boiler (hot water and heating)
Short Rotation Coppice biomass willow plantation to supply our own logs
Rainwater runoff harvesting
Solar lighting
Water usage reduction
All electricity used is from 100% renewable sources
Off grid composting toilets
Recycled brick and concrete in the car parks
Willow Spiling (River bank protection)
Woodland management and replanting
Waste reduction & recycling point
Habitat improvement programme

The designer must be able to supply all images and graphics as part of the award. Only your own work will be accepted. Not images and designs by others.
Nice to have
• Colour schemes
Eggshell blue (9ADCED), Dark Blue (1F6991) and white
(Taken from our logo)

Green & Gold
(Moss Riders in the film Verdant)

```html
<!DOCTYPE html>
<html lang="en">
<head>
<meta charset="utf-8">
<title>Thistlebrook Hollow – Family Nature Adventure Stay</title>
<link rel="stylesheet" href="https://fonts.googleapis.com/css2?family=Arvo:wght@400;700&family=Tinos&family=Arimo&display=swap">
<style>
  :root {
    --eggshell: #9adced;
    --dark-blue: #1f6991;
    --footer-blue: #1d5f86;
    --white: #ffffff;
    --nav-line: #d2d2d2;
    --nav-text: #222222;
    --forest-dark: #1d3a14;
    --forest-mid: #3d6424;
    --forest-light: #6e9a3c;
    --charcoal: #242424;
    --charcoal-deep: #161616;
    --muted-grey: #5b5b5b;
    --badge-grey: #4a4a4a;
    --badge-light: #bdbdbd;
    --divider: #7fbfd2;
    --body-ink: #111111;
  }
  * { box-sizing: border-box; margin: 0; padding: 0; }
  html, body { width: 1103px; height: 1200px; overflow: hidden; background: var(--white); }
  .canvas { position: relative; width: 1103px; height: 1200px; overflow: hidden; font-family: "Tinos", serif; }

  /* Navigation */
  .site-nav { position: absolute; top: 0; left: 0; width: 1103px; height: 43px; background: linear-gradient(#ffffff, #e9e9e9); border-bottom: 1px solid var(--nav-line); z-index: 5; }
  .site-nav ul { list-style: none; position: absolute; left: 169px; top: 0; display: flex; height: 43px; border-left: 1px solid var(--nav-line); }
  .site-nav li { font-family: "Arvo", serif; font-size: 10.5px; text-transform: uppercase; color: var(--nav-text); padding: 0 10px; line-height: 43px; border-right: 1px solid var(--nav-line); white-space: nowrap; }
  .site-nav li.is-current { background: var(--eggshell); color: var(--dark-blue); }

  /* Hero slider */
  .hero { position: absolute; top: 43px; left: 0; width: 1103px; height: 570px; }
  .hero-photo { position: absolute; inset: 0; background:
      radial-gradient(ellipse at 55% 40%, var(--forest-light) 0%, transparent 55%),
      linear-gradient(180deg, var(--forest-mid) 0%, var(--forest-dark) 45%, var(--forest-mid) 80%, var(--forest-light) 100%); }
  .hero-caption { position: absolute; top: 220px; left: 0; width: 1103px; text-align: center; font-family: "Arvo", serif; font-weight: 700; font-size: 24px; line-height: 28px; color: var(--white); text-transform: uppercase; text-shadow: 0 1px 3px rgba(0,0,0,.6); }
  .slider-arrow { position: absolute; top: 225px; width: 50px; height: 50px; border: 2px solid var(--white); }
  .slider-arrow.prev { left: 167px; }
  .slider-arrow.next { left: 887px; background: var(--eggshell); opacity: .9; }
  .slider-arrow svg { width: 100%; height: 100%; display: block; }

  /* Brand mark */
  .brand { position: absolute; left: 451px; top: 405px; width: 200px; height: 200px; border-radius: 50%; background: var(--eggshell); border: 4px solid var(--white); display: flex; align-items: center; justify-content: center; text-align: center; z-index: 3; }
  .brand-name { font-family: "Arvo", serif; font-size: 21px; line-height: 26px; color: var(--dark-blue); font-weight: 400; }

  /* Intro */
  .intro { position: absolute; top: 590px; left: 0; width: 1103px; height: 301px; background: var(--eggshell); }
  .intro-divider { position: absolute; left: 551px; top: 20px; height: 270px; border-left: 1px dashed var(--divider); }
  .intro-col { position: absolute; top: 90px; width: 360px; text-align: center; }
  .intro-col.who { left: 175px; }
  .intro-col.what { left: 568px; }
  .intro-col h2 { font-family: "Arvo", serif; font-weight: 700; font-size: 25px; color: var(--white); letter-spacing: .5px; margin-bottom: 20px; }
  .intro-col p { font-size: 13.6px; line-height: 15px; color: var(--body-ink); }

  /* Partners */
  .partners { position: absolute; top: 891px; left: 0; width: 1103px; height: 122px; background: var(--charcoal); }
  .partner-badge { position: absolute; top: 36px; height: 50px; background: var(--badge-grey); border-radius: 4px; }
  .partner-badge.is-active { background: var(--badge-light); }

  /* Contact band */
  .contact-band { position: absolute; top: 1013px; left: 0; width: 1103px; height: 70px; background: var(--charcoal-deep); }
  .contact-item { position: absolute; top: 18px; display: flex; align-items: center; gap: 12px; font-family: "Arvo", serif; font-weight: 700; font-size: 26px; color: var(--muted-grey); text-transform: uppercase; white-space: nowrap; }
  .contact-item.call { left: 156px; }
  .contact-item.beaches { left: 640px; }
  .contact-icon { width: 36px; height: 36px; }

  /* Footer */
  .site-footer { position: absolute; top: 1083px; left: 0; width: 1103px; height: 117px; background: var(--footer-blue); font-family: "Arimo", sans-serif; color: var(--white); }
  .footer-links { position: absolute; left: 158px; top: 38px; display: flex; gap: 10px; font-size: 12.2px; list-style: none; white-space: nowrap; }
  .copyright { position: absolute; left: 158px; top: 61px; font-size: 12px; }
  .social { position: absolute; left: 862px; top: 30px; display: flex; flex-direction: column; gap: 6px; font-size: 12px; line-height: 16px; }
  .social-link { display: flex; align-items: center; gap: 6px; white-space: nowrap; }
  .social-dot { width: 14px; height: 14px; border-radius: 50%; background: var(--white); flex: none; }
</style>
</head>
<body>
<div class="canvas">

  <nav class="site-nav">
    <ul>
      <li class="is-current">Home</li>
      <li>Accommodation &amp; Booking</li>
      <li>Location &amp; Interactive Map</li>
      <li>Activities &amp; Events</li>
      <li>Meet the Residents</li>
      <li>Green Credentials</li>
    </ul>
  </nav>

  <section class="hero">
    <div class="hero-photo" role="img" aria-label="Family with backpacks walking across a log bridge through a green forest"></div>
    <p class="hero-caption">Etiam non felis mi. Quisque<br>feugiat consectetur,</p>
    <div class="slider-arrow prev">
      <svg viewBox="0 0 50 50"><polyline points="29,15 19,25 29,35" fill="none" stroke="#fff" stroke-width="3"/></svg>
    </div>
    <div class="slider-arrow next">
      <svg viewBox="0 0 50 50"><polyline points="21,15 31,25 21,35" fill="none" stroke="#fff" stroke-width="3"/></svg>
    </div>
  </section>

  <div class="brand"><span class="brand-name">Thistlebrook<br>Hollow</span></div>

  <section class="intro">
    <div class="intro-divider"></div>
    <div class="intro-col who">
      <h2>WHO WE ARE</h2>
      <p>Lorem ipsum dolor sit amet, consectetur adipiscing elit. Sed id tempus enim. Etiam eros velit, rutrum in fringilla id, fermentum sit amet nulla. Nullam cursus mi ut lorem commodo eu pharetra elit blandit. Phasellus malesuada, massa et adipiscing tempor, tellus lacus vulputate dui, non commodo mi neque a dui.</p>
    </div>
    <div class="intro-col what">
      <h2>WHAT WE DO</h2>
      <p>Praesent enim dolor, iaculis ut molestie vitae, tempus vitae tortor. Vestibulum ante ipsum primis in faucibus orci luctus et ultrices posuere cubilia CuraeIn vel turpis lacus, vitae fringilla urna. Etiam et tellus vel turpis cursus egestas ut vel risus. Nunc sapien lorem, pretium a sodales sit amet, dictum id tellus. In ante mauris,</p>
    </div>
  </section>

  <section class="partners" aria-label="Partners: Heritage Keepers, Woodland Stewardship Board, Amberhill Lands, Eco Enterprise Honours">
    <div class="partner-badge" style="left:212px;width:44px;"></div>
    <div class="partner-badge is-active" style="left:378px;width:156px;"></div>
    <div class="partner-badge" style="left:645px;width:48px;"></div>
    <div class="partner-badge" style="left:790px;width:98px;"></div>
  </section>

  <section class="contact-band">
    <div class="contact-item call">
      <svg class="contact-icon" viewBox="0 0 36 36"><circle cx="18" cy="18" r="18" fill="#5b5b5b"/><path d="M12 9c1.5-1 3-.5 3.5 1l1.2 3c.3 1-.2 1.8-1 2.3l-1 .6c.8 2.4 2.6 4.3 5 5.2l.7-1c.6-.8 1.5-1.1 2.4-.7l2.8 1.3c1.4.6 1.7 2.2.7 3.4-1.6 1.9-4 2.3-6.4 1.2C14.2 23.5 10 18.6 9.5 13.8c-.2-1.9.8-3.7 2.5-4.8z" fill="#161616"/></svg>
      <span>Call us : 000-000-0000</span>
    </div>
    <div class="contact-item beaches">
      <svg class="contact-icon" viewBox="0 0 36 36"><circle cx="18" cy="18" r="18" fill="#5b5b5b"/><path d="M6 22c4-3 8-3 12 0s8 3 12 0v4c-4 3-8 3-12 0s-8-3-12 0z" fill="#161616"/><circle cx="22" cy="12" r="4" fill="#161616"/></svg>
      <span>Nearby beaches</span>
    </div>
  </section>

  <footer class="site-footer">
    <ul class="footer-links">
      <li>Home</li>
      <li>Accommodation &amp; Booking</li>
      <li>Location &amp; Interactive Map</li>
      <li>Activities &amp; Events</li>
      <li>Meet the Residents</li>
      <li>Green Credentials</li>
    </ul>
    <p class="copyright">© Copyright Thistlebrook Hollow 2013. All Rights Reserved.</p>
    <div class="social">
      <span class="social-link"><span class="social-dot"></span>Friendbook</span>
      <span class="social-link"><span class="social-dot"></span>Chirper</span>
    </div>
  </footer>

</div>
</body>
</html>
```